Bright Nook

Create effective banner ads for the website BrightNook.com. We are building a re-target ad for coffee shops and/or stay at home office workers, and we would like to order 3 separate designs with the banner sizes 300x250, 728x90, 320x50, 640x100, 300x50, and 160x600, and they all need to be under 40kb of data. We have provided 9 slogans you can use in the Banner Ad Slogans and Extra Details document. Feel free to create your own slogan, and use resources found on our website.

Industry/Entity Type

Building

```html
<!DOCTYPE html>
<html lang="en">
<head>
<meta charset="UTF-8">
<title>Bright Nook – Banner</title>
<link href="https://fonts.googleapis.com/css2?family=Exo+2:wght@300;700;800&family=Playball&display=block" rel="stylesheet">
<style>
  :root {
    --orange: #e8731a;
    --orange-light: #f08a2a;
    --orange-deep: #d9601a;
    --red: #d8361f;
    --white: #ffffff;
    --photo-dark: #2b2622;
    --photo-mid: #5e4a3a;
    --photo-light: #8c7d72;
  }
  html, body {
    margin: 0;
    padding: 0;
    width: 1200px;
    height: 998px;
    overflow: hidden;
    background: #ffffff;
  }
  .banner {
    position: relative;
    width: 1200px;
    height: 998px;
    overflow: hidden;
    font-family: "Exo 2", sans-serif;
    color: var(--white);
  }
  .lounge-photo {
    position: absolute;
    inset: 0;
    background:
      radial-gradient(ellipse at 70% 55%, var(--photo-light) 0%, transparent 45%),
      linear-gradient(160deg, #3a3430 0%, var(--photo-mid) 45%, #a06a3e 70%, var(--photo-dark) 100%);
  }
  .facets {
    position: absolute;
    inset: 0;
  }
  .headline {
    position: absolute;
    left: 80px;
    top: 62px;
    margin: 0;
    font-family: "Playball", "Yellowtail", cursive;
    font-weight: 400;
    font-size: 112px;
    line-height: 124px;
    white-space: nowrap;
  }
  .tagline {
    position: absolute;
    left: 93px;
    top: 382px;
    margin: 0;
    font-size: 38px;
    font-weight: 300;
    line-height: 54px;
  }
  .tagline strong {
    display: block;
    font-weight: 700;
  }
  .cta-button {
    position: absolute;
    left: 42px;
    top: 692px;
    width: 420px;
    height: 104px;
    box-sizing: border-box;
    border-radius: 52px;
    border: 5px solid #8a5a2a;
    background: linear-gradient(180deg, var(--orange-light) 0%, var(--orange) 55%, var(--orange-deep) 100%);
    display: flex;
    align-items: center;
    justify-content: center;
    font-size: 64px;
    font-weight: 800;
    text-shadow: 0 2px 3px rgba(0,0,0,.35);
    text-decoration: none;
    color: var(--white);
  }
  .cta-note {
    position: absolute;
    left: 90px;
    top: 822px;
    margin: 0;
    font-size: 37px;
    font-weight: 700;
    line-height: 48px;
    text-shadow: 0 2px 4px rgba(0,0,0,.7);
  }
  .brand-badge {
    position: absolute;
    left: 848px;
    top: 660px;
    width: 268px;
    height: 268px;
    box-sizing: border-box;
    border: 5px solid var(--white);
    border-radius: 50%;
    display: flex;
    align-items: center;
    justify-content: center;
  }
  .brand-name {
    font-size: 34px;
    font-weight: 700;
    color: var(--white);
  }
</style>
</head>
<body>
<div class="banner">
  <div class="lounge-photo" role="img" aria-label="Photo of two men working on phones in orange leather lounge chairs in a modern coworking lounge"></div>

  <svg class="facets" width="1200" height="998" viewBox="0 0 1200 998" aria-hidden="true">
    <polygon points="0,0 860,0 890,185 830,310 560,480 124,540 36,670 0,580" fill="#e8731a"/>
    <polygon points="0,0 520,0 300,360 0,420" fill="#f08a2a" opacity=".55"/>
    <polygon points="860,0 890,185 740,120" fill="#f39b3c" opacity=".6"/>
    <polygon points="560,480 830,310 610,330" fill="#f08a2a" opacity=".5"/>
    <polygon points="0,500 124,540 36,670 0,640" fill="#d8361f"/>
    <polygon points="124,540 560,480 300,470" fill="#e24e1e" opacity=".7"/>
    <polygon points="0,420 300,360 124,540 0,500" fill="#de5f1c" opacity=".6"/>

    <g fill="none" stroke="#ffffff" stroke-width="14" opacity=".35">
      <polyline points="548,740 598,785 548,830"/>
      <polyline points="620,740 670,785 620,830"/>
      <polyline points="692,740 742,785 692,830"/>
    </g>
  </svg>

  <h1 class="headline">Coffee Shops are<br>for Socializing</h1>
  <p class="tagline">Get Real Work Done at <strong>Bright Nook</strong></p>

  <a class="cta-button" href="#">Click here</a>
  <p class="cta-note">to schedule a Tour and<br>get a Free Day Pass</p>

  <div class="brand-badge"><span class="brand-name">Bright Nook</span></div>
</div>
</body>
</html>
```